Billboard for Local Roofing Company

The billboard we are using will be 12' tall and 24' wide. We are looking for a clean design that is not too busy, one that stands out and is easily readable. The branding colors used should match the colors in our logo. On the billboard, it should have our slogan "Where Every Shingle Thing Matters" with the word "Shingle" in the orange.
It should also have the DRK Summit Circle logo uploaded here as well.
Lastly, it should have our phone number 555-274-1938 and our website www.quelmont-roofing.example.
I have uploaded a stock image we are thinking about using in the background of the sign...this could be darkened or otherwise obscured.
- Match fonts up if possible

```html
<!DOCTYPE html>
<html lang="en">
<head>
<meta charset="utf-8">
<title>Quelmont Roofing Billboard</title>
<link rel="stylesheet" href="https://fonts.googleapis.com/css2?family=Montserrat:wght@600;700;800;900&display=swap">
<style>
  :root {
    --page: #d9d9d9;
    --bar: #1e1f1f;
    --orange: #e55623;
    --white: #ffffff;
    --shadow: #111111;
    --roof-light: #4a4a4d;
    --roof-dark: #1c1c1e;
    --seal: #6a6b6f;
  }
  html, body {
    margin: 0;
    width: 1200px;
    height: 849px;
    overflow: hidden;
    background: var(--page);
  }
  .billboard {
    position: absolute;
    left: 0;
    top: 124px;
    width: 1200px;
    height: 600px;
    display: block;
    font-family: "Montserrat", Arial, sans-serif;
  }
  .headline { font-weight: 800; fill: var(--white); }
  .headline-accent {
    fill: var(--orange);
    font-weight: 800;
    filter: drop-shadow(4px 4px 0 var(--shadow));
  }
  .brand-name { font-weight: 800; fill: var(--white); }
  .contact-phone { font-weight: 700; fill: var(--white); }
  .contact-web { font-weight: 600; fill: var(--white); }
</style>
</head>
<body>
<svg class="billboard" viewBox="0 0 1200 600" xmlns="http://www.w3.org/2000/svg">
  <defs>
    <linearGradient id="roofTone" x1="0" y1="0" x2="1" y2="1">
      <stop offset="0" stop-color="var(--roof-light)"/>
      <stop offset="0.55" stop-color="#333336"/>
      <stop offset="1" stop-color="var(--roof-dark)"/>
    </linearGradient>
  </defs>

  <rect class="background-photo" x="0" y="0" width="1200" height="499" fill="url(#roofTone)"
        role="img" aria-label="Darkened photo of asphalt shingle rooftops with gables"/>

  <rect class="accent-rule" x="0" y="492" width="1200" height="7" fill="var(--orange)"/>
  <rect class="contact-bar" x="0" y="499" width="1200" height="101" fill="var(--bar)"/>

  <g class="brand">
    <rect x="819" y="138" width="24" height="24" fill="var(--orange)"/>
    <text class="brand-name" x="853" y="162" font-size="33" textLength="301" lengthAdjust="spacingAndGlyphs">Quelmont Roofing</text>
  </g>

  <text class="headline" x="90" y="229" font-size="96" textLength="657" lengthAdjust="spacingAndGlyphs">Where Every</text>
  <text class="headline-accent" x="90" y="341" font-size="100" textLength="412" lengthAdjust="spacingAndGlyphs">Shingle</text>
  <text class="headline" x="537" y="341" font-size="82" textLength="567" lengthAdjust="spacingAndGlyphs">Thing Matters</text>

  <circle class="certification-seal" cx="144" cy="479" r="72" fill="var(--seal)"
          role="img" aria-label="DRK Summit Circle certification seal"/>

  <text class="contact-phone" x="231" y="573" font-size="60" textLength="405" lengthAdjust="spacingAndGlyphs">555-274-1938</text>
  <rect class="contact-divider" x="670" y="529" width="5" height="45" fill="var(--white)"/>
  <text class="contact-web" x="704" y="564" font-size="30" textLength="462" lengthAdjust="spacingAndGlyphs">www.quelmont-roofing.example</text>
</svg>
</body>
</html>
```